Brintell's Business Card

I need some designs for a new business card including the new logo attached. An old example of our business card is also attached to show all the data that should be included on the new design.
**I added some more examples someone had mocked up**

Contact Information for Business Card

Should include all info on other examples uploaded.

```html
<!DOCTYPE html>
<html lang="en">
<head>
<meta charset="utf-8">
<title>Brintell's Business Card</title>
<link href="https://fonts.googleapis.com/css2?family=Montserrat:wght@500;600;700&family=Oswald:wght@600&display=swap" rel="stylesheet">
<style>
  :root {
    --bg: #3a3a3a;
    --brand-blue: #0b6fbd;
    --brand-blue-light: #1f86cf;
    --brand-red: #e31b23;
    --paper: #ffffff;
  }
  * { box-sizing: border-box; margin: 0; padding: 0; }
  html, body { width: 1200px; height: 1200px; overflow: hidden; }
  body {
    background: var(--bg);
    position: relative;
    font-family: "Montserrat", sans-serif;
  }
  .card {
    position: absolute;
    left: 220px;
    width: 760px;
    height: 434px;
    border-radius: 34px;
    overflow: hidden;
    background: var(--paper);
  }
  .card--contact { top: 120px; background: linear-gradient(135deg, var(--brand-blue-light), var(--brand-blue)); }
  .card--brand { top: 646px; }
  .card svg.shape { position: absolute; inset: 0; width: 100%; height: 100%; }

  .contact-block {
    position: absolute;
    left: 415px;
    top: 78px;
    right: 24px;
    color: var(--paper);
  }
  .contact-name {
    font-weight: 600;
    font-size: 32px;
    letter-spacing: 1px;
    white-space: nowrap;
    margin-bottom: 14px;
  }
  .contact-list { list-style: none; }
  .contact-list li {
    display: flex;
    align-items: center;
    gap: 10px;
    font-size: 19px;
    font-weight: 500;
    white-space: nowrap;
    margin-bottom: 6px;
  }
  .contact-list svg { width: 18px; height: 18px; flex: none; }
  .credentials {
    margin-top: 34px;
    font-family: "Oswald", sans-serif;
    font-weight: 600;
    font-size: 24px;
    line-height: 1.2;
    white-space: nowrap;
    text-transform: uppercase;
  }

  .brand-lockup {
    position: absolute;
    left: 80px;
    top: 70px;
  }
  .brand-name {
    display: flex;
    align-items: center;
    gap: 16px;
    color: var(--brand-blue);
    font-weight: 700;
    font-size: 64px;
    line-height: 1;
    letter-spacing: 1px;
  }
  .brand-dot {
    width: 48px; height: 48px;
    border-radius: 50%;
    background: var(--brand-blue);
  }
  .brand-tagline {
    margin: 10px 0 0 64px;
    color: var(--brand-red);
    font-weight: 600;
    font-size: 16px;
    letter-spacing: 0.5px;
    text-transform: uppercase;
    white-space: nowrap;
  }
  .service-area {
    position: absolute;
    right: 60px;
    bottom: 34px;
    color: var(--paper);
    font-family: "Oswald", sans-serif;
    font-weight: 600;
    font-size: 26px;
    text-transform: uppercase;
    letter-spacing: 0.5px;
    white-space: nowrap;
  }
</style>
</head>
<body>

  <section class="card card--contact">
    <svg class="shape" viewBox="0 0 760 434" preserveAspectRatio="none" aria-hidden="true">
      <path d="M0 0 L170 0 C300 40 400 150 395 250 C390 350 320 415 250 434 L0 434 Z" fill="var(--paper)"/>
    </svg>
    <div class="contact-block">
      <h1 class="contact-name">DYLAN BRINTELL</h1>
      <ul class="contact-list">
        <li>
          <svg viewBox="0 0 24 24" fill="#fff"><path d="M6.6 10.8a15 15 0 0 0 6.6 6.6l2.2-2.2a1 1 0 0 1 1-.25 11.4 11.4 0 0 0 3.6.57 1 1 0 0 1 1 1V20a1 1 0 0 1-1 1A17 17 0 0 1 3 4a1 1 0 0 1 1-1h3.5a1 1 0 0 1 1 1c0 1.25.2 2.45.57 3.57a1 1 0 0 1-.25 1z"/></svg>
          555.014.2287
        </li>
        <li>
          <svg viewBox="0 0 24 24" fill="none" stroke="#fff" stroke-width="2"><rect x="2" y="5" width="20" height="14"/><path d="M2 5l10 8 10-8"/></svg>
          service@brintellair.com
        </li>
        <li>
          <svg viewBox="0 0 24 24" fill="none" stroke="#fff" stroke-width="1.8"><circle cx="12" cy="12" r="10"/><ellipse cx="12" cy="12" rx="4.5" ry="10"/><path d="M2 12h20M4 7h16M4 17h16"/></svg>
          www.brintellair.com
        </li>
      </ul>
      <p class="credentials">Licensed &amp; Insured<br>Family Owned &amp; Operated</p>
    </div>
  </section>

  <section class="card card--brand">
    <svg class="shape" viewBox="0 0 760 434" preserveAspectRatio="none" aria-hidden="true">
      <path d="M0 270 C200 360 420 372 560 200 C620 130 700 80 760 60 L760 434 L0 434 Z" fill="var(--brand-red)"/>
      <path d="M0 284 C200 374 420 386 560 214 C620 144 700 94 760 74 L760 434 L0 434 Z" fill="var(--paper)"/>
      <path d="M0 300 C200 390 420 400 560 230 C620 160 700 110 760 90 L760 434 L0 434 Z" fill="var(--brand-blue)"/>
    </svg>
    <div class="brand-lockup">
      <div class="brand-name"><span class="brand-dot"></span>Brintell's</div>
      <p class="brand-tagline">Air Conditioning &amp; Heating Service</p>
    </div>
    <p class="service-area">Serves Ashford Falls, IA &amp; Surrounding Areas</p>
  </section>

</body>
</html>
```